Steel Company / Iron Railing Business Card Template

We are a custom steel fabrication company located in Ashcombe, WR. In business since 1979, we recently developed a new logo, and we're looking for a business card design to help display the new logo and our business. The name of the company is Kelbrook Forge Co.. The Office Phone number is (555) 555-0143. We fabricate and install custom "wrought iron" railings on our residential side, we also fabricate and erect structural steel (think cranes and steel beams in buildings) on our commercial side. Looking to get a business card template designed. Something modern, but professional. Clear and easy to read. Front should have all business and employee information including phone number(s), email address, business information, etc. back should spotlight logo.

Industry/Entity Type

Construction / Home Improvement

Contact Information for Business Card

Business information is Kelbrook Forge Co., 48 Dunmore Ave Suite 3305, Ashcombe, WR 19074. Phone number is (555) 555-0143. Website is www.kelbrookforge.example Business card should be for "Tom Pelling" with the job title "Sales & Estimating" but be editable for other employees. Tom's phone number is (555) 555-0178

Colors

Designer to choose colors to be used in the design.

Requirements
Must have
• Modern Feel, Design should be sized for standard business card sizing 3.5" x 2" (88.9mm x 50.8mm)

```html
<!DOCTYPE html>
<html lang="en">
<head>
<meta charset="utf-8">
<title>Kelbrook Forge Co. — Business Card</title>
<link href="https://fonts.googleapis.com/css2?family=Montserrat:wght@700;800&family=Lato:wght@400&display=swap" rel="stylesheet">
<style>
  :root {
    --navy: #2e3a87;
    --red: #c0202a;
    --ink: #2a2a2a;
    --paper: #ffffff;
    --backdrop: #e4e5e9;
  }
  * { margin: 0; padding: 0; box-sizing: border-box; }
  html, body { width: 1200px; height: 880px; overflow: hidden; }
  body { background: var(--backdrop); position: relative; font-family: "Lato", sans-serif; }

  .card {
    position: absolute;
    width: 560px; height: 320px;
    border-radius: 22px;
    overflow: hidden;
    box-shadow: 0 10px 28px rgba(0,0,0,0.18);
  }
  .card--back { left: 60px; top: 80px; background: var(--navy); }
  .card--front { left: 580px; top: 470px; background: var(--paper); }

  .brand {
    position: absolute;
    display: flex; align-items: center; gap: 12px;
    font-family: "Montserrat", sans-serif; font-weight: 800;
  }
  .card--back .brand { left: 0; right: 0; top: 0; bottom: 0; justify-content: center; color: var(--paper); font-size: 38px; }
  .card--front .brand { right: 38px; top: 58px; color: var(--navy); font-size: 24px; }
  .brand__dot { border-radius: 50%; background: var(--red); flex: none; }
  .card--back .brand__dot { width: 26px; height: 26px; }
  .card--front .brand__dot { width: 18px; height: 18px; }

  .divider { position: absolute; height: 1px; background: var(--ink); }
  .divider--main { left: 140px; right: 36px; top: 140px; }
  .divider--short { left: 40px; width: 150px; top: 208px; }

  .person { position: absolute; left: 40px; top: 150px; }
  .person__name { font-family: "Montserrat", sans-serif; font-weight: 700; font-size: 24px; color: var(--navy); line-height: 1.1; }
  .person__title { font-size: 14px; color: var(--ink); margin-top: 2px; }

  .contacts { position: absolute; left: 40px; top: 216px; list-style: none; font-size: 14px; color: var(--ink); }
  .contacts li { display: flex; align-items: center; gap: 8px; height: 21px; }
  .contacts svg { width: 13px; height: 13px; fill: var(--red); flex: none; }

  .address { position: absolute; right: 36px; top: 152px; text-align: right; font-size: 13px; color: var(--ink); line-height: 1.45; }

  .bands { position: absolute; left: 0; top: 0; width: 560px; height: 320px; }
  .website { position: absolute; right: 36px; bottom: 14px; color: var(--paper); font-size: 13px; }
</style>
</head>
<body>

  <section class="card card--back" aria-label="Card back">
    <div class="brand"><span class="brand__dot"></span>Kelbrook Forge Co.</div>
  </section>

  <section class="card card--front" aria-label="Card front">
    <svg class="bands" viewBox="0 0 560 320" aria-hidden="true">
      <path d="M0 296 L318 296 Q330 296 336 284 L346 266 L356 266 L346 284 Q338 304 322 304 L0 304 Z" fill="var(--red)"/>
      <path d="M0 308 L330 308 Q345 308 352 290 Q360 268 380 268 L560 268 L560 320 L0 320 Z" fill="var(--navy)"/>
    </svg>

    <div class="brand"><span class="brand__dot"></span>Kelbrook Forge Co.</div>

    <div class="divider divider--main"></div>

    <div class="person">
      <div class="person__name">Tom Pelling</div>
      <div class="person__title">Sales &amp; Estimating</div>
    </div>
    <div class="divider divider--short"></div>

    <ul class="contacts">
      <li><svg viewBox="0 0 24 24"><path d="M6.6 10.8a15.1 15.1 0 0 0 6.6 6.6l2.2-2.2a1 1 0 0 1 1-.25 11.4 11.4 0 0 0 3.6.57 1 1 0 0 1 1 1V20a1 1 0 0 1-1 1A17 17 0 0 1 3 4a1 1 0 0 1 1-1h3.5a1 1 0 0 1 1 1c0 1.25.2 2.45.57 3.57a1 1 0 0 1-.25 1z"/></svg>(555) 555-0178</li>
      <li><svg viewBox="0 0 24 24"><path d="M6.6 10.8a15.1 15.1 0 0 0 6.6 6.6l2.2-2.2a1 1 0 0 1 1-.25 11.4 11.4 0 0 0 3.6.57 1 1 0 0 1 1 1V20a1 1 0 0 1-1 1A17 17 0 0 1 3 4a1 1 0 0 1 1-1h3.5a1 1 0 0 1 1 1c0 1.25.2 2.45.57 3.57a1 1 0 0 1-.25 1z"/></svg>(555) 555-0143</li>
      <li><svg viewBox="0 0 24 24"><path d="M2 5h20v14H2z M2 5l10 8 10-8" stroke="#fff" stroke-width="1.5"/></svg>info@kelbrookforge.example</li>
    </ul>

    <div class="address">
      Kelbrook Forge Co., 48 Dunmore Ave<br>
      Suite 3305, Ashcombe, WR 19074
    </div>

    <div class="website">www.kelbrookforge.example</div>
  </section>

</body>
</html>
```